Coralmere Crystal Works manufacturer needs a label design

Our company is Coralmere Crystal Works Company and we have chosen to use "Tidevale" as our brand. Our web site is www.coralmerecrystalworks.example.au

We need a label design for a clear PET jar which will contain our Natural Sea Salt Flakes. The design should include the following descriptive nouns - Australian, Natural, Sea Salt Flakes.

The design should also include "100% Australian made and owned". The design may include a high quality photo of flake salt. The final design should communicate the natural pure qualities of our flake salt.

The following aspects differentiate our product from everyone else: We use seawater brine, More seawater minerals, magnesium etc in our product, no insolubles, no additives, our product dissolves quickly. Our manufacturing process uses old fashioned artisan open pan crystallization in a modern format.

Target Market(s)

Consumer / Retail

Industry/Entity Type

It Company

Font styles to use
Serif
Sans Serif
Decorative
Script

Requirements
Must have
• "Tidevale" branding. It should also have nouns such as Australian, Natural, Sea Salt Flakes, 100% Australian made and owned. The label must also include "240g Net" Weight. The label dimensions are: height 65mm, width 50mm
• The look and feel I'm looking for is per the bottle label included in the attachments below
Nice to have
• Picture of flake salt in a bowl
Should not have
• Nothing comes to mind

```html
<!DOCTYPE html>
<html lang="en">
<head>
<meta charset="utf-8">
<title>Tidevale Sea Salt Flakes Label – Coralmere Crystal Works Company</title>
<link rel="stylesheet" href="https://fonts.googleapis.com/css2?family=Roboto:ital,wght@0,400;0,500;0,700;1,700&display=swap">
<style>
  :root {
    --page: #ffffff;
    --cream: #f7eed9;
    --navy: #2b3992;
    --navy-deep: #1f2a78;
    --ink: #1c2a6e;
    --sky-light: #f4f9ff;
    --sky-mid: #a9c8ec;
    --sky-edge: #5f8fd0;
    --salt: #ffffff;
    --salt-shade: #d6e3f2;
  }
  html, body {
    margin: 0;
    padding: 0;
    width: 1200px;
    height: 2456px;
    overflow: hidden;
    background: var(--page);
  }
  .label-canvas {
    display: block;
    width: 1200px;
    height: 2456px;
  }
  .arc-tagline {
    font-family: "Roboto", Arial, sans-serif;
    font-weight: 700;
    font-style: italic;
    font-size: 34px;
    fill: var(--ink);
  }
  .maker-line, .maker-suffix {
    font-family: "Roboto", Arial, sans-serif;
    font-weight: 500;
    font-size: 28px;
    letter-spacing: 6px;
    fill: var(--ink);
  }
  .maker-suffix { letter-spacing: 12px; }
  .brand-main {
    font-family: "Roboto", Arial, sans-serif;
    font-weight: 700;
    font-size: 110px;
    fill: var(--ink);
  }
  .net-weight {
    font-family: "Roboto", Arial, sans-serif;
    font-weight: 400;
    font-size: 32px;
    fill: var(--ink);
  }
  .rule { stroke: var(--ink); stroke-width: 3; }
</style>
</head>
<body>
<svg class="label-canvas" viewBox="0 0 1200 2456" xmlns="http://www.w3.org/2000/svg">
  <defs>
    <linearGradient id="panelGradient" x1="0" y1="0" x2="0" y2="1">
      <stop offset="0" stop-color="var(--navy-deep)"/>
      <stop offset="1" stop-color="var(--navy)"/>
    </linearGradient>
    <radialGradient id="seal-fill" cx="0.5" cy="0.55" r="0.55">
      <stop offset="0" stop-color="var(--sky-light)"/>
      <stop offset="0.55" stop-color="var(--sky-mid)"/>
      <stop offset="1" stop-color="var(--sky-edge)"/>
    </radialGradient>
    <radialGradient id="salt-fill" cx="0.5" cy="0.4" r="0.6">
      <stop offset="0" stop-color="var(--salt)"/>
      <stop offset="1" stop-color="var(--salt-shade)"/>
    </radialGradient>
    <path id="tagline-arc" d="M 222 1240 A 378 378 0 0 1 978 1240"/>
  </defs>

  <g class="label">
    <rect class="label-border" x="150" y="643" width="900" height="1170" fill="var(--cream)"/>
    <rect class="label-panel" x="180" y="673" width="840" height="1110" fill="url(#panelGradient)"/>
    <rect class="label-panel-line" x="194" y="687" width="812" height="1082" fill="none" stroke="var(--cream)" stroke-width="3"/>

    <circle class="seal-ring" cx="600" cy="1240" r="442" fill="var(--cream)"/>
    <circle class="seal-face" cx="600" cy="1240" r="420" fill="url(#seal-fill)"/>

    <text class="arc-tagline">
      <textPath href="#tagline-arc" startOffset="50%" text-anchor="middle">Natural Sea Salt Flakes • 100% Australian Made and Owned</textPath>
    </text>

    <text class="maker-line" x="603" y="1082" text-anchor="middle">CORALMERE CRYSTAL WORKS</text>
    <line class="rule" x1="330" y1="1104" x2="870" y2="1104"/>
    <text class="brand-main" x="600" y="1198" text-anchor="middle">Tidevale</text>
    <line class="rule" x1="330" y1="1224" x2="870" y2="1224"/>
    <text class="maker-suffix" x="606" y="1264" text-anchor="middle">COMPANY</text>

    <ellipse class="salt-photo" role="img" aria-label="Photo of sea salt flakes in a glass bowl with a wooden spoon"
             cx="600" cy="1440" rx="270" ry="120" fill="url(#salt-fill)"/>

    <text class="net-weight" x="600" y="1610" text-anchor="middle">240g Net</text>
  </g>
</svg>
</body>
</html>
```